International Lifestyle Real Estate Brokerage Needs Eye Catching Website

We need a new website for a cutting edge / dynamic real estate startup, Palmcrest Homes, that will serve as a concierge brokerage to assist cold weather residents with the research, selection, financing and purchase of vacation / retirement properties in warm weather climates in the US and then globally. We will have personally vetted all properties to insure that our clients are only getting the best of the best with no hidden surprises.

** The website design will ultimately need to be coded into a wordpress theme.

We are not locked into any specific colour scheme but would prefer something warm vs cold as that is really the lifestyle we are selling. We like lots of white negative space and hope to allow high end photography to provide most of the pop in colour.

I have attached mock up wire frames to demonstrate desired functionality for three pages we need designed

1) Home Page
2) Market Profile (City overview and developments)
3) Community Profile Page (Individual development profile)

I have also included .ai file for the logo. Not locked into red.

Final design should communicate excitement, lifestyle while maintaining an air of professionalism and reliability. We have developed over 30 sites and have high expectations for the winning design.

Regards,
Dan

Target Market(s)

Canadian and Northern US residents looking to purchase vacation or retirement real estate in warmer climates, initially in the US, but eventually Internationally.

Industry/Entity Type

Real Estate

Contact Information for Business Card

Names for Business Cards

Dan Fairholt
604.555.2716
dan@palmcresthomes.ca

Coding

Coded - Design and coding required

Number of Pages Required

3 page

Font styles to use
Serif
Sans Serif

Requirements
Must have
• See wireframe documents uploaded.
• Site design will ultimately be coded into a child theme to function on a selected wordpress theme. If the designer has a Wordpres Theme in mind that would be compatible with the design we would appreciate that information.
Nice to have
• See wireframe documents uploaded. Prefer clean, modern site, white negative space, bold photography will add most of the colour and pop.
Should not have
• Anything cartoony or sophmoric.

```html
<!DOCTYPE html>
<html lang="en">
<head>
<meta charset="utf-8">
<title>Palmcrest Homes</title>
<link href="https://fonts.googleapis.com/css2?family=Oswald:wght@400;500&family=Lato:wght@400;700&display=swap" rel="stylesheet">
<style>
:root{
  --red:#d7262b;
  --navy:#0b2f6b;
  --black:#0d0d0d;
  --ink:#222;
  --muted:#555;
  --paper:#f5f5f5;
  --footer:#3d3d3f;
  --footer-text:#d8d8d8;
}
*{box-sizing:border-box;margin:0;padding:0}
html,body{width:1200px;height:3267px;overflow:hidden}
body{position:relative;background:var(--paper);font-family:'Lato',sans-serif;color:var(--ink)}
.abs{position:absolute}
.heading{font-family:'Oswald',sans-serif;font-weight:400;color:var(--ink);text-transform:uppercase}

/* header */
.header{left:0;top:0;width:1200px;height:163px;background:linear-gradient(90deg,#0a2a63,#1553a8 70%,#0a2a63)}
.top-links{left:770px;top:0;width:298px;height:32px;background:var(--black);display:flex;justify-content:space-around;align-items:center;font-size:12px;font-weight:700;color:#fff;letter-spacing:.5px}
.phone{left:880px;top:52px;display:flex;align-items:center;gap:12px;color:#fff;font-size:22px;font-weight:700}
.main-nav{left:0;top:109px;width:1200px;height:54px;background:var(--black)}
.main-nav span{position:absolute;top:18px;font-size:14px;font-weight:700;color:#fff;letter-spacing:.5px}
.logo{left:111px;top:17px;width:190px;height:131px;background:#fff;display:flex;flex-direction:column;align-items:center;justify-content:center;gap:6px}
.logo-name{font-family:'Oswald',sans-serif;font-weight:500;color:var(--red);font-size:25px;letter-spacing:2px;text-align:center;line-height:1.15}
.logo-mark{width:12px;height:12px;background:var(--red)}

/* hero */
.hero{left:0;top:163px;width:1200px;height:547px;background:linear-gradient(180deg,#1b3c7a 0%,#6a5a4a 45%,#a8813d 62%,#2ea9b5 85%,#3b6b3a 100%)}
.hero-arrow{top:410px}
.hero-title{left:0;top:545px;width:1200px;text-align:center;font-family:'Oswald',sans-serif;font-size:50px;color:#fff;letter-spacing:1px}
.hero-sub{left:0;top:617px;width:1200px;text-align:center;font-size:28px;color:#fff}

/* services */
.services{left:0;top:710px;width:1200px;height:449px;background:linear-gradient(180deg,#c9d6ea,#e6ebf2 60%,#d8dccb)}
.services-veil{left:0;top:710px;width:1200px;height:449px;background:rgba(255,255,255,.55)}
.section-title{width:1200px;left:0;text-align:center;font-size:34px}
.underline{width:70px;height:3px;background:var(--red);left:565px}
.services-lead{left:0;top:826px;width:1200px;text-align:center;font-size:15px;color:#333}
.service{width:200px;text-align:center;top:890px}
.service-ring{width:96px;height:96px;margin:0 auto;border-radius:50%;border:3px solid var(--red);background:#fff;display:flex;align-items:center;justify-content:center}
.service-label{margin-top:20px;font-size:22px;color:#222}
.btn{left:518px;top:1069px;width:162px;height:46px;background:var(--red);color:#fff;font-size:21px;display:flex;align-items:center;justify-content:center;border-radius:2px}

/* featured development */
.dev-photo{left:111px;top:1313px;width:640px;height:401px;background:linear-gradient(160deg,#264066,#5a5770 40%,#b98a5a 65%,#2a8fa0 100%)}
.dev-panel{left:751px;top:1313px;width:338px;height:401px;background:#e9ebef;padding:44px 20px 0 22px}
.dev-name{font-size:24px;font-weight:700;color:var(--red)}
.dev-text{margin-top:10px;font-size:13px;line-height:1.5;color:#555;width:260px}
.dev-row{display:flex;align-items:center;margin-top:18px;font-size:15px;color:#333}
.dev-row svg{margin-right:12px}
.dev-row .count{margin-left:auto;margin-right:52px;width:30px;height:30px;border-radius:50%;background:#9a9a9a;color:#fff;font-size:14px;display:flex;align-items:center;justify-content:center}
.dev-nav{left:872px;top:1630px;display:flex;gap:24px}

/* markets */
.markets-title{left:111px;top:1766px;font-size:31px}
.tab{top:1777px;height:34px;padding:0 14px;display:flex;align-items:center;font-size:15px;color:#333;border-bottom:1px solid #ccc}
.tab.active{background:var(--red);color:#fff;border:none}
.tile{width:316px;height:267px}
.tile-label{position:absolute;left:0;bottom:0;width:100%;height:42px;background:rgba(10,25,55,.82);border-top:3px solid var(--red);color:#fff;font-size:18px;display:flex;align-items:center;justify-content:center;letter-spacing:.5px}
.commitment{background:linear-gradient(180deg,#3a3f48,#23272e);color:#fff;text-align:center;padding:34px 30px 0}
.commitment h3{font-family:'Lato',sans-serif;font-weight:400;font-size:19px;letter-spacing:.5px}
.commitment .rule{width:46px;height:2px;background:var(--red);margin:10px auto 14px}
.commitment p{font-size:15px;line-height:1.55;color:#eee}

/* blog */
.blog-title{left:111px;top:2478px;font-size:31px}
.post{top:2585px;width:316px}
.post-img{width:316px;height:155px;position:relative}
.post-date{position:absolute;left:3px;top:3px;width:44px;height:52px;background:var(--red);color:#fff;text-align:center;font-weight:700;line-height:1}
.post-date b{display:block;font-size:22px;padding-top:5px}
.post-date i{font-style:normal;font-size:12px}
.post h4{margin-top:22px;font-size:14px;font-weight:700;color:#222}
.post p{margin-top:10px;font-size:12.5px;line-height:1.55;color:#555}
.post a{display:block;margin-top:12px;font-size:13px;color:var(--red);text-decoration:none}

/* footer */
.footer{left:0;top:2905px;width:1200px;height:318px;background:var(--footer);color:var(--footer-text)}
.f-title{font-size:21px;color:#fff;top:2952px}
.f-title em{font-style:normal;color:var(--red)}
.f-links{top:3000px;left:114px;list-style:none;font-size:13px;line-height:37px}
.f-links li::before{content:"•";margin-right:10px}
.f-contact{top:3003px;left:322px;font-size:13px;line-height:1.5}
.f-contact .row{display:flex;gap:12px;margin-bottom:12px}
.field{left:622px;width:232px;height:34px;background:#fff;border-radius:2px;font-size:11px;color:#999;padding:10px 8px}
.submit{left:622px;top:3139px;width:126px;height:34px;background:var(--red);color:#fff;font-size:16px;font-weight:700;display:flex;align-items:center;justify-content:center}
.f-logo{left:912px;top:3060px;width:180px;text-align:center;font-family:'Oswald',sans-serif;font-size:24px;color:#c9c9c9;letter-spacing:3px;line-height:1.2}
.copybar{left:0;top:3223px;width:1200px;height:44px;background:var(--red);color:#fff;font-size:13px;padding:14px 0 0 113px}
.social{top:3228px;width:34px;height:34px;border-radius:50%;background:#fff}
</style>
</head>
<body>

<!-- header -->
<div class="abs header"></div>
<div class="abs top-links"><span>SAVED</span><span>ABOUT</span><span>CONTACT</span><span>LOGIN</span></div>
<div class="abs phone">
  <svg width="34" height="34" viewBox="0 0 34 34"><circle cx="17" cy="17" r="15" fill="none" stroke="#fff" stroke-width="2"/><path d="M12 10l3 0 1 4-2 1.5c1 2 2.5 3.5 4.5 4.5L20 18l4 1 0 3c0 1-1 2-2 2-6 0-11-5-11-11 0-1 1-3 1-3z" fill="#fff"/></svg>
  <span>012.555.0148</span>
</div>
<div class="abs main-nav">
  <span style="left:522px">SEARCH</span>
  <span style="left:655px">OUR PROCESS</span>
  <span style="left:832px">RESOURCES</span>
  <span style="left:995px">REGISTER</span>
</div>
<div class="abs logo">
  <div class="logo-mark"></div>
  <div class="logo-name">PALMCREST<br>HOMES</div>
</div>

<!-- hero -->
<div class="abs hero" role="img" aria-label="Luxury villa with lit pool terrace at dusk"></div>
<svg class="abs hero-arrow" style="left:44px" width="20" height="40" viewBox="0 0 20 40"><path d="M16 4L4 20l12 16" fill="none" stroke="#fff" stroke-width="2"/></svg>
<svg class="abs hero-arrow" style="left:1134px" width="20" height="40" viewBox="0 0 20 40"><path d="M4 4l12 16L4 36" fill="none" stroke="#fff" stroke-width="2"/></svg>
<div class="abs hero-title">LIFE IS TOO SHORT TO BE COLD</div>
<div class="abs hero-sub">Where do you want to play in sunshine</div>

<!-- services -->
<div class="abs services" role="img" aria-label="Softly blurred view of a white resort residence"></div>
<div class="abs services-veil"></div>
<h2 class="abs heading section-title" style="top:740px">Services We Provide</h2>
<div class="abs underline" style="top:798px"></div>
<p class="abs services-lead">Lorem ipsum dolor sit amet, consectetuer adipisemy nibh euismod tincidunt utre magmi aliquam erat volutpat.</p>

<div class="abs service" style="left:133px">
  <div class="service-ring"><svg width="48" height="48" viewBox="0 0 48 48"><path d="M8 24L24 10l16 14" fill="none" stroke="#222" stroke-width="3"/><rect x="14" y="24" width="20" height="14" fill="#222"/><rect x="21" y="29" width="6" height="9" fill="#fff"/></svg></div>
  <div class="service-label">For Buyers</div>
</div>
<div class="abs service" style="left:377px">
  <div class="service-ring"><svg width="48" height="48" viewBox="0 0 48 48"><path d="M6 24L22 10l14 12" fill="none" stroke="#222" stroke-width="3"/><rect x="11" y="24" width="16" height="14" fill="#222"/><circle cx="34" cy="32" r="9" fill="#fff" stroke="#222" stroke-width="2.5"/><text x="34" y="37" font-size="13" font-family="Lato,sans-serif" font-weight="700" text-anchor="middle" fill="#222">$</text></svg></div>
  <div class="service-label">For Sellers</div>
</div>
<div class="abs service" style="left:621px">
  <div class="service-ring"><svg width="48" height="48" viewBox="0 0 48 48"><path d="M8 12h32M14 12v28M30 12v10" stroke="#222" stroke-width="3" fill="none"/><rect x="24" y="26" width="14" height="14" fill="#222"/><rect x="6" y="38" width="36" height="3" fill="#222"/></svg></div>
  <div class="service-label">Developments</div>
</div>
<div class="abs service" style="left:865px">
  <div class="service-ring"><svg width="48" height="48" viewBox="0 0 48 48"><path d="M6 24L22 10l16 14" fill="none" stroke="#222" stroke-width="3"/><rect x="12" y="24" width="20" height="14" fill="#222"/><circle cx="33" cy="30" r="7" fill="#fff" stroke="#222" stroke-width="2.5"/><path d="M38 35l5 5" stroke="#222" stroke-width="3"/></svg></div>
  <div class="service-label">Property Survey</div>
</div>
<div class="abs btn">Learn More</div>

<!-- featured developments -->
<h2 class="abs heading section-title" style="top:1205px">Featured Developments</h2>
<div class="abs underline" style="top:1264px;background:#bbb"></div>
<div class="abs dev-photo" role="img" aria-label="Development villa with pool and lounge daybed at twilight"></div>
<div class="abs dev-panel">
  <div class="dev-name">Coral Tower, Survey, NJ</div>
  <p class="dev-text">Lorem ipsum dolor sit amet, consectetuer adipisemy nibh euismod tincidunt utre.</p>
  <div class="dev-row"><svg width="18" height="16" viewBox="0 0 18 16"><path d="M1 8h16v3a4 4 0 0 1-4 4H5a4 4 0 0 1-4-4z M4 8V3a2 2 0 0 1 4 0" fill="none" stroke="#555" stroke-width="1.5"/></svg>Bathrooms<span class="count">2</span></div>
  <div class="dev-row"><svg width="18" height="16" viewBox="0 0 18 16"><path d="M1 3v12M1 10h16v5M3 8h5V6H3z" fill="none" stroke="#555" stroke-width="1.5"/></svg>Beds<span class="count">3</span></div>
  <div class="dev-row"><svg width="18" height="16" viewBox="0 0 18 16"><path d="M1 7L9 1l8 6v8H1z M5 15V9h8v6" fill="none" stroke="#555" stroke-width="1.5"/></svg>Garages<span class="count">2</span></div>
  <div class="dev-row"><svg width="18" height="18" viewBox="0 0 18 18"><path d="M9 1a6 6 0 0 1 6 6c0 4-6 10-6 10S3 11 3 7a6 6 0 0 1 6-6z" fill="var(--red)"/><circle cx="9" cy="7" r="2" fill="#fff"/></svg>United States / Minnesota</div>
</div>
<div class="abs dev-nav">
  <svg width="16" height="24" viewBox="0 0 16 24"><path d="M12 3L4 12l8 9" fill="none" stroke="#222" stroke-width="3"/></svg>
  <svg width="16" height="24" viewBox="0 0 16 24"><path d="M4 3l8 9-8 9" fill="none" stroke="#222" stroke-width="3"/></svg>
</div>

<!-- featured markets -->
<h2 class="abs heading markets-title">Featured Markets</h2>
<div class="abs tab active" style="left:599px">UNITED STATES</div>
<div class="abs tab" style="left:779px">MEXICO</div>
<div class="abs tab" style="left:906px">SOUTH AMERICA</div>

<div class="abs tile" style="left:111px;top:1877px;background:linear-gradient(180deg,#5a8fd0,#8aa26a 45%,#c9a77a 65%,#2aa7c8)" role="img" aria-label="Orlando villa with palms and pool"><div class="tile-label">ORLANDO</div></div>
<div class="abs tile" style="left:442px;top:1877px;background:linear-gradient(160deg,#2a1a12,#6b3a20 50%,#b8743a)" role="img" aria-label="Naples living room with fireplace"><div class="tile-label">NAPLES</div></div>
<div class="abs tile" style="left:773px;top:1877px;background:linear-gradient(180deg,#c0643a,#e7a65a 45%,#8a5a3a 80%,#3a3a3a)" role="img" aria-label="Fort Myers mansion at sunset"><div class="tile-label">FORT MEYERS</div></div>
<div class="abs tile" style="left:111px;top:2161px;background:linear-gradient(180deg,#0f2040,#2a3b5a 40%,#c89a50 75%,#3a4a3a)" role="img" aria-label="Clearwater modern home lit at night"><div class="tile-label">CLEARWATER</div></div>
<div class="abs tile" style="left:442px;top:2161px;background:linear-gradient(180deg,#1f4a8a,#3a68a8 45%,#d8cdbb 70%,#4a5a4a)" role="img" aria-label="Asheville estate under blue evening sky"><div class="tile-label">ASHEVILLE</div></div>
<div class="abs tile commitment" style="left:773px;top:2161px">
  <h3>OUR COMMITMENT</h3>
  <div class="rule"></div>
  <p>Lorem ipsum dolor sit amet, consectetuer adipisemy nibh euismod tincidunt utre magmi aliquam erat volutpat. iat nulla .</p>
</div>

<!-- blog -->
<h2 class="abs heading blog-title">Recent Blog Posts</h2>
<div class="abs underline" style="left:111px;top:2530px;width:40px;background:#bbb"></div>

<div class="abs post" style="left:111px">
  <div class="post-img" role="img" aria-label="Resort home with pool at dusk" style="background:linear-gradient(180deg,#5a6a8a,#b07a40 55%,#2a9ac0)"><div class="post-date"><b>22</b><i>JUN</i></div></div>
  <h4>Sed ut perspiciatis unde istemo</h4>
  <p>Duis autem vel eum iriure dolor in hendrerit inkvulpu ate velit esse molestie facilisis.</p>
  <a>Read More &nbsp;››</a>
</div>
<div class="abs post" style="left:442px">
  <div class="post-img" role="img" aria-label="Villa courtyard pool in evening light" style="background:linear-gradient(180deg,#6a8ab0,#d8c0a0 50%,#3aa0c0)"><div class="post-date"><b>22</b><i>JUN</i></div></div>
  <h4>Sed ut perspiciatis unde istemo</h4>
  <p>Duis autem vel eum iriure dolor in hendrerit inkvulpu ate velit esse molestie facilisis.</p>
  <a>Read More &nbsp;››</a>
</div>
<div class="abs post" style="left:773px">
  <div class="post-img" role="img" aria-label="Bright bedroom with red accents" style="background:linear-gradient(160deg,#e8e8e8,#b8b8b8 50%,#6a6a6a)"><div class="post-date"><b>22</b><i>JUN</i></div></div>
  <h4>Sed ut perspiciatis unde istemo</h4>
  <p>Duis autem vel eum iriure dolor in hendrerit inkvulpu ate velit esse molestie facilisis.</p>
  <a>Read More &nbsp;››</a>
</div>

<!-- footer -->
<div class="abs footer"></div>
<div class="abs f-title" style="left:113px">Quick <em>Links</em></div>
<ul class="abs f-links"><li>Home</li><li>About</li><li>Our Process</li><li>Resources</li><li>Contact</li></ul>

<div class="abs f-title" style="left:322px">Contact <em>Details</em></div>
<div class="abs f-contact">
  <div class="row"><svg width="14" height="16" viewBox="0 0 14 16"><path d="M7 1a5 5 0 0 1 5 5c0 4-5 9-5 9S2 10 2 6a5 5 0 0 1 5-5z" fill="#ddd"/></svg><div>PALMCREST HOMES<br>123, Ut wisi enim ad veniam,<br>Mor nostrni tation -123 456</div></div>
  <div class="row" style="margin-top:10px"><svg width="14" height="14" viewBox="0 0 14 14"><path d="M2 1h3l1 3-2 1c1 2 2 3 4 4l1-2 3 1v3c0 1-1 2-2 2C5 13 1 9 1 3c0-1 1-2 1-2z" fill="#ddd"/></svg><b>(123) 555 0192</b></div>
  <div class="row"><svg width="14" height="14" viewBox="0 0 14 14"><rect x="3" y="1" width="8" height="4" fill="#ddd"/><rect x="1" y="5" width="12" height="6" fill="#ddd"/><rect x="3" y="9" width="8" height="4" fill="#fff"/></svg>(123) 555 0192</div>
  <div class="row"><svg width="14" height="12" viewBox="0 0 14 12"><rect x="1" y="1" width="12" height="10" fill="none" stroke="#ddd" stroke-width="1.5"/><path d="M1 1l6 5 6-5" fill="none" stroke="#ddd" stroke-width="1.5"/></svg>info@palmcresthomes.ca</div>
</div>

<div class="abs f-title" style="left:622px">Quick <em>Inquiry</em></div>
<div class="abs field" style="top:3008px">Name</div>
<div class="abs field" style="top:3053px">Email</div>
<div class="abs field" style="top:3098px">Message</div>
<div class="abs submit">Submit</div>

<div class="abs f-logo">PALMCREST<br>HOMES</div>

<div class="abs copybar">Copyright © 2016 PALMCREST HOMES. All Rights Reserved.</div>
<div class="abs social" style="left:962px"></div>
<div class="abs social" style="left:1006px"></div>
<div class="abs social" style="left:1051px"></div>

</body>
</html>
```